The bright tart company. Wholesale gourmet pies to hospitality, needs a logo and flyer design

We need a flyer design for a new company based in Canberra ACT, called "the bright tart company' Our flyer needs to describe our range of products, and delivery details. Our logo we would like to encompass a cartoon style chefs hat, love heart and pie. We like the idea of using red somewhere .

```html
<!DOCTYPE html>
<html lang="en">
<head>
<meta charset="utf-8">
<title>The Bright Tart Company – Pie Menu Flyer</title>
<link rel="stylesheet" href="https://fonts.googleapis.com/css2?family=Special+Elite&family=Playball&family=Oswald:wght@300&family=Arimo:wght@400;700&display=swap">
<style>
  :root {
    --red: #e3090f;
    --red-dark: #a80006;
    --white: #ffffff;
    --ink: #1b1b1b;
    --grey: #c9c9c9;
    --wood-light: #e2b27a;
    --wood-mid: #cf9559;
    --wood-dark: #b87a3f;
    --band: #161616;
    --pie-orange: #f28a4c;
  }
  * { box-sizing: border-box; margin: 0; padding: 0; }
  html, body { width: 797px; height: 1200px; overflow: hidden; background: #eeeeee; }
  .flyer {
    position: relative; width: 797px; height: 1200px; overflow: hidden;
    background: linear-gradient(100deg, var(--wood-light) 0%, var(--wood-mid) 45%, var(--wood-light) 70%, var(--wood-dark) 100%);
    font-family: "Special Elite", "Courier New", monospace;
  }
  .header-shapes { position: absolute; inset: 0; width: 797px; height: 1200px; }
  .brand {
    position: absolute; left: 60px; top: 136px; display: flex; align-items: center; gap: 14px;
  }
  .brand-dot { width: 46px; height: 46px; border-radius: 50%; background: var(--red); flex: none; }
  .brand-name {
    font-family: "Oswald", "Arial Narrow", sans-serif; font-weight: 300;
    font-size: 22px; color: var(--ink); letter-spacing: 1px; white-space: nowrap;
  }
  .hero-pie {
    position: absolute; left: 450px; top: 62px; width: 285px; height: 180px;
    border-radius: 48% 48% 40% 40%;
    background: radial-gradient(ellipse at 50% 35%, #f7a36e 0%, var(--pie-orange) 55%, #9fb4bd 100%);
  }
  .headline {
    position: absolute; left: 34px; top: 254px; font-size: 60px; font-weight: 400; color: var(--white);
    letter-spacing: 2px; transform: rotate(5deg); transform-origin: left center; white-space: nowrap;
  }
  .section-title { position: absolute; font-size: 27px; font-weight: 400; letter-spacing: 1px; white-space: nowrap; }
  .section-title.sweet { left: 42px; top: 372px; color: var(--red); }
  .section-title.savory { right: 48px; top: 404px; color: var(--ink); }
  .menu-item {
    position: absolute; height: 78px; border-radius: 40px; display: flex; align-items: center;
    font-family: "Playball", cursive; font-size: 30px; white-space: nowrap;
    box-shadow: 0 4px 8px rgba(0,0,0,.35);
  }
  .menu-item.light { background: linear-gradient(90deg, var(--grey) 0%, var(--white) 45%, var(--white) 100%); color: var(--ink); }
  .menu-item.dark { background: linear-gradient(180deg, #ff2a2a 0%, var(--red) 55%, var(--red-dark) 100%); color: var(--white); }
  .sweet-item { left: 60px; width: 300px; padding-left: 62px; }
  .savory-item { left: 440px; width: 300px; padding-left: 26px; font-size: 28px; }
  .savory-item.light { background: linear-gradient(270deg, var(--grey) 0%, var(--white) 45%, var(--white) 100%); }
  .menu-item.small { font-size: 22px; }
  .photo {
    position: absolute; top: 50%; width: 94px; height: 94px; margin-top: -47px; border-radius: 50%;
    border: 4px solid var(--white); box-shadow: 0 0 0 3px var(--red), 0 3px 8px rgba(0,0,0,.4);
  }
  .sweet-item .photo { left: -34px; }
  .savory-item .photo { right: -34px; }
  .footer { position: absolute; left: 0; bottom: 0; width: 797px; height: 96px; background: var(--band); }
  .order-panel {
    position: absolute; right: 0; bottom: 0; width: 392px; height: 142px; background: var(--band);
    border-top-left-radius: 60px; padding: 22px 0 0 40px;
  }
  .order-label { color: var(--white); font-size: 26px; letter-spacing: 1px; white-space: nowrap; }
  .order-phone {
    font-family: "Arimo", Arial, sans-serif; font-weight: 700; color: var(--red);
    font-size: 31px; margin-top: 12px; white-space: nowrap;
  }
  .contact { position: absolute; left: 50px; bottom: 18px; font-family: "Arimo", Arial, sans-serif; color: var(--white); font-size: 19px; line-height: 30px; }
  .contact-row { display: flex; align-items: center; gap: 10px; white-space: nowrap; }
  .contact-row svg { width: 14px; height: 14px; flex: none; }
</style>
</head>
<body>
<main class="flyer">
  <svg class="header-shapes" viewBox="0 0 797 1200" aria-hidden="true">
    <defs>
      <linearGradient id="bannerFill" x1="0" y1="0" x2="0" y2="1">
        <stop offset="0" stop-color="#f01a1a"/>
        <stop offset="1" stop-color="#b00008"/>
      </linearGradient>
    </defs>
    <polygon points="0,0 797,0 797,310 0,240" fill="#ffffff"/>
    <polygon points="0,222 797,292 797,388 0,308" fill="url(#bannerFill)"/>
  </svg>

  <div class="brand">
    <span class="brand-dot"></span>
    <span class="brand-name">THE BRIGHT TART COMPANY</span>
  </div>
  <div class="hero-pie" role="img" aria-label="Cartoon illustration of a pie with a slice cut out"></div>

  <h1 class="headline">CHOOSE YOUR WOW PIE</h1>

  <h2 class="section-title sweet">SWEET PIES</h2>
  <h2 class="section-title savory">SAVORY PIES</h2>

  <div class="menu-item light sweet-item" style="top:429px"><span class="photo" role="img" aria-label="Photo of pumpkin pie" style="background:radial-gradient(#e8a04a,#7a4a22)"></span>Pumpkin Pie</div>
  <div class="menu-item dark sweet-item" style="top:543px"><span class="photo" role="img" aria-label="Photo of apple pie" style="background:radial-gradient(#d9a566,#8a5a30)"></span>Apple Pie</div>
  <div class="menu-item light sweet-item" style="top:663px"><span class="photo" role="img" aria-label="Photo of blueberry pie" style="background:radial-gradient(#c9c3cf,#3b2d55)"></span>Blueberry Pie</div>
  <div class="menu-item dark sweet-item" style="top:781px"><span class="photo" role="img" aria-label="Photo of pecan pie" style="background:radial-gradient(#a3622b,#4a2a12)"></span>Pecan Pie</div>
  <div class="menu-item light sweet-item" style="top:897px"><span class="photo" role="img" aria-label="Photo of key lime pie" style="background:radial-gradient(#f1ecd8,#a99e84)"></span>Keylime Pie</div>
  <div class="menu-item dark sweet-item small" style="top:1011px"><span class="photo" role="img" aria-label="Photo of banana cream pie" style="background:radial-gradient(#fbf6ec,#c9b89a)"></span>Banana Cream Pie</div>

  <div class="menu-item light savory-item" style="top:460px"><span class="photo" role="img" aria-label="Photo of chicken pot pies" style="background:radial-gradient(#edc894,#9a6a3a)"></span>Chicken pot Pie</div>
  <div class="menu-item dark savory-item small" style="top:575px"><span class="photo" role="img" aria-label="Photo of butternut squash pie" style="background:radial-gradient(#e69a3a,#8a4a14)"></span>Butternut Squash</div>
  <div class="menu-item light savory-item" style="top:692px"><span class="photo" role="img" aria-label="Photo of spinach pie" style="background:radial-gradient(#d8c7a6,#3d4a2a)"></span>Spinach Pie</div>
  <div class="menu-item dark savory-item" style="top:808px"><span class="photo" role="img" aria-label="Photo of Reuben pies" style="background:radial-gradient(#a25a2a,#4a2410)"></span>Ruben Pie</div>
  <div class="menu-item light savory-item small" style="top:929px"><span class="photo" role="img" aria-label="Photo of vegetable pot pie" style="background:radial-gradient(#e2a862,#9a5e28)"></span>Vegetable Pot Pie</div>

  <footer class="footer"></footer>
  <div class="order-panel">
    <p class="order-label">To order for pickup</p>
    <p class="order-phone">Call (954) 555-0182</p>
  </div>
  <div class="contact">
    <p class="contact-row"><svg viewBox="0 0 14 14" aria-hidden="true"><circle cx="7" cy="7" r="6" fill="none" stroke="#e3090f" stroke-width="1.6"/><path d="M1 7h12M7 1c-3 3-3 9 0 12M7 1c3 3 3 9 0 12" fill="none" stroke="#e3090f" stroke-width="1.2"/></svg>www.thebrighttartcompany.net</p>
    <p class="contact-row"><svg viewBox="0 0 14 14" aria-hidden="true"><rect x="1" y="3" width="12" height="8" fill="#e3090f"/><path d="M1 3l6 5 6-5" fill="none" stroke="#161616" stroke-width="1.2"/></svg>info@brighttartcompany.com.au</p>
  </div>
</main>
</body>
</html>
```